Website design for staffing/workforce solutions company - Harbor Crest Solutions

Create a launch-ready website
Harbor Crest Solutions also known as HCS. This is a company that specializes in Staffing/Work force solutions for Healthcare/IT/Logistics/Maintenance/Construction/Manufacturing/Industrial/General Labor. HCS works with government agencies/contracts also. Use the attached logo in the build of the website. Website should be clean, modern, engaging, innovative. Website needs to speak to the professional services industry.
Harbor Crest Solutions or HCS is a certified VOSB, SDVOSB, DBE and Minority-Owned Business.
The website needs to be compliant for government contracting.

Website needs to include the following--
Modern UI/UX Enhancements: A hero section with a strong call-to-action.
Government Contracting Compliance: Certification display and a Capability Statement download.
Advanced Careers Section: A dedicated job application portal.
Social Media & Lead Generation: Links to Workvine, Quillo, and Pagebloom.
Security & Performance: Optimized for SEO, fast loading, and mobile responsiveness.
1. Modern Design Upgrades
๐Ÿ”น Upgrade UI/UX for a Professional, Trustworthy Look
โœ… Full-width hero banner with a high-quality background image representing business, technology, and workforce solutions.
โœ… Animated elements (subtle transitions for smooth browsing experience).
โœ… Bold CTA buttons for easy navigation to key actions (e.g., โ€œGet Startedโ€ or โ€œRequest a Consultationโ€).
โœ… Dark-themed header with contrasting colors (professional & government-trustworthy).
โœ… New Homepage Hero Section Example:
"Your Trusted Partner in Workforce, IT, Maintenance & Logistics Solutions"
Button: "Discover Our Services"

2. Enhanced Government Contracting Section (Key for Compliance)
๐Ÿ“Œ Essential for securing contracts & building credibility
โœ… Capability Statement (Downloadable PDF)

Showcase key past contracts, company qualifications, and services in a downloadable format for government buyers.
โœ… Certifications Display (VOSB, SDVOSB, DBE, Minority-Owned Business)

Visual badge display to emphasize legitimacy for government contracts.
โœ… Procurement Readiness Details

NAICS Codes, DUNS Number, CAGE Code, and relevant KPR.example registration details.
โœ… Past Performance Showcase (Case Studies Section)

Highlight successful projects and government contracts.
โœ… Compliance & Security

Add SOC 2, HIPAA (for healthcare staffing), and ITAR compliance if applicable.
3. Advanced Job Search & Candidate Portal (For Staffing Services)
๐Ÿ“Œ To attract top talent for staffing contracts

โœ… Advanced Job Search Feature

Filters: Industry, location, job type (contract/full-time), salary range, and clearance level (for government jobs).
โœ… Candidate Login Portal

Applicants can upload resumes, track applications, and receive job alerts.
โœ… Employer Portal (For Businesses Hiring Through HCS)

A dedicated section for companies to submit staffing requests and view candidate matches.
4. Service-Specific Landing Pages (SEO & Engagement)
๐Ÿ“Œ Helps different industries find relevant services faster

๐Ÿ”น Dedicated Pages for Each Service:
โœ… Staffing & Workforce Solutions

Specialized sections for Healthcare, IT, Construction, Industrial, and General Labor staffing.
โœ… IT Services

List services like Cybersecurity, Cloud Solutions, and IT Consulting.
Showcase tech stack & certifications.
โœ… Logistics & Maintenance

Detail fleet management, supply chain services, and industrial maintenance.
โœ… Government Contracting Solutions

A streamlined page for government agencies.
5. Security & Compliance Upgrades (For Government Work)
๐Ÿ“Œ To ensure compliance & credibility in government contracting

โœ… SSL Certification (100% Required for Security)

Secure client and job applicant data.
โœ… ADA Compliance (Accessibility)

Ensure the website follows WCAG 2.1 accessibility standards for government clients.
โœ… GDPR & Data Protection Features

A privacy policy and terms of service to comply with data regulations.
6. Performance & Mobile Optimization
๐Ÿ“Œ To ensure fast loading & responsiveness

โœ… Mobile-Responsive Design

Optimized for mobile-friendly navigation since many users browse from phones.
โœ… Fast-Loading Pages

Optimize images & implement lazy loading for better site speed.
โœ… SEO-Optimized Pages

Improve search ranking on Findoro with:
Keyword-optimized content (e.g., โ€œGovernment Contracting Staffing Servicesโ€)
Schema markup for job listings
Blog/articles about staffing trends
7. Social Media & Lead Generation
๐Ÿ“Œ For brand credibility & client engagement

โœ… Workvine, Quillo, Pagebloom Integration

Display recent updates from Workvine (primary for B2B & government).
โœ… Lead Capture Forms

Forms for business inquiries, talent applications, and government RFPs.
โœ… Client & Candidate Testimonials
Showcase client success stories & employee experiences

Good websites to pull examples for inspiration/direction--
https://www.vlmn.example/
https://www.torvana.example/
https://brightmeridian.example/homepage/
https://www.valdorcheck.example/capability-statement

Industry/Entity Type

Staffing/Professional Services

Coding

Coded - Design and coding required

Number of Pages Required

5+ page

Requirements
Must have
• Website needs to include the following-- Modern UI/UX Enhancements: A hero section with a strong call-to-action. Government Contracting Compliance: Certification display and a Capability Statement download. Advanced Careers Section: A dedicated job application portal. Social Media & Lead Generation: Links to Workvine, Quillo, and Pagebloom. Security & Performance: Optimized for SEO, fast loading, and mobile responsiveness. 1. Modern Design Upgrades ๐Ÿ”น Upgrade UI/UX for a Professional, Trustworthy Look โœ… Full-width hero banner with a high-quality background image representing business, technology, and workforce solutions. โœ… Animated elements (subtle transitions for smooth browsing experience). โœ… Bold CTA buttons for easy navigation to key actions (e.g., โ€œGet Startedโ€ or โ€œRequest a Consultationโ€). โœ… Dark-themed header with contrasting colors (professional & government-trustworthy). โœ… New Homepage Hero Section Example: "Your Trusted Partner in Workforce, IT, & Logistics Solutions" Button: "Discover Our Services" 2. Enhanced Government Contracting Section (Key for Compliance) ๐Ÿ“Œ Essential for securing contracts & building credibility โœ… Capability Statement (Downloadable PDF) Showcase key past contracts, company qualifications, and services in a downloadable format for government buyers. โœ… Certifications Display (VOSB, SDVOSB, DBE, Minority-Owned Business) Visual badge display to emphasize legitimacy for government contracts. โœ… Procurement Readiness Details NAICS Codes, DUNS Number, CAGE Code, and relevant KPR.example registration details. โœ… Past Performance Showcase (Case Studies Section) Highlight successful projects and government contracts. โœ… Compliance & Security Add SOC 2, HIPAA (for healthcare staffing), and ITAR compliance if applicable. 3. Advanced Job Search & Candidate Portal (For Staffing Services) ๐Ÿ“Œ To attract top talent for staffing contracts โœ… Advanced Job Search Feature Filters: Industry, location, job type (contract/full-time), salary range, and clearance level (for government jobs). โœ… Candidate Login Portal Applicants can upload resumes, track applications, and receive job alerts. โœ… Employer Portal (For Businesses Hiring Through HCS) A dedicated section for companies to submit staffing requests and view candidate matches. 4. Service-Specific Landing Pages (SEO & Engagement) ๐Ÿ“Œ Helps different industries find relevant services faster ๐Ÿ”น Dedicated Pages for Each Service: โœ… Staffing & Workforce Solutions Specialized sections for Healthcare, IT, Construction, Industrial, and General Labor staffing. โœ… IT Services List services like Cybersecurity, Cloud Solutions, and IT Consulting. Showcase tech stack & certifications. โœ… Logistics & Maintenance Detail fleet management, supply chain services, and industrial maintenance. โœ… Government Contracting Solutions A streamlined page for government agencies. 5. Security & Compliance Upgrades (For Government Work) ๐Ÿ“Œ To ensure compliance & credibility in government contracting โœ… SSL Certification (100% Required for Security) Secure client and job applicant data. โœ… ADA Compliance (Accessibility) Ensure the website follows WCAG 2.1 accessibility standards for government clients. โœ… GDPR & Data Protection Features A privacy policy and terms of service to comply with data regulations. 6. Performance & Mobile Optimization ๐Ÿ“Œ To ensure fast loading & responsiveness โœ… Mobile-Responsive Design Optimized for mobile-friendly navigation since many users browse from phones. โœ… Fast-Loading Pages Optimize images & implement lazy loading for better site speed. โœ… SEO-Optimized Pages Improve search ranking on Findoro with: Keyword-optimized content (e.g., โ€œGovernment Contracting Staffing Servicesโ€) Schema markup for job listings Blog/articles about staffing trends 7. Social Media & Lead Generation ๐Ÿ“Œ For brand credibility & client engagement โœ… Workvine, Quillo, Pagebloom Integration Display recent updates from Workvine (primary for B2B & government). โœ… Lead Capture Forms Forms for business inquiries, talent applications, and government RFPs. โœ… Client & Candidate Testimonials Showcase client success stories & employee experiences Good websites to pull examples for inspiration/direction-- https://www.vlmn.example/ https://www.torvana.example/ https://brightmeridian.example/homepage/

```html
<!DOCTYPE html>
<html lang="en">
<head>
<meta charset="UTF-8">
<title>Harbor Crest Solutions — Workforce, IT &amp; Logistics</title>
<link href="https://fonts.googleapis.com/css2?family=Lato:wght@400;700;900&family=Montserrat:wght@500;600;700&display=swap" rel="stylesheet">
<style>
:root{
  --red:#c8141b;
  --red-deep:#b80f15;
  --navy:#0b1456;
  --navy-btn:#101a6b;
  --dark:#1f1f1f;
  --footer:#1b1b1b;
  --strip:#f2f2f2;
  --grey:#dcdcdc;
  --ink:#111;
  --muted:#333;
  --white:#fff;
  --check:#2d8cf0;
}
*{box-sizing:border-box;margin:0;padding:0}
html,body{width:1200px;height:2831px;overflow:hidden}
body{position:relative;font-family:'Lato',sans-serif;color:var(--ink);background:var(--white)}
.abs{position:absolute}

/* header */
.site-header{position:absolute;left:0;top:0;width:1200px;height:60px;background:var(--dark)}
.brand{position:absolute;left:159px;top:18px;color:var(--red);font-weight:900;font-size:19px;letter-spacing:.3px;display:flex;align-items:center;gap:7px}
.brand .mark{width:12px;height:12px;background:var(--red)}
.main-nav{position:absolute;top:0;height:60px;display:flex;align-items:center}
.main-nav a{position:absolute;color:var(--white);text-decoration:none;font-size:16px;white-space:nowrap}
.menu-toggle{position:absolute;left:1017px;top:28px}

/* hero */
.hero{position:absolute;left:0;top:60px;width:1200px;height:529px}
.hero-photo{position:absolute;inset:0;background:linear-gradient(90deg,#c9a454 0%,#8d7c62 18%,#b7a894 30%,#9f9488 70%,#7e6d5f 85%,#bdb4aa 100%)}
.hero-panel{position:absolute;left:346px;top:60px;width:508px;height:561px;background:rgba(196,18,24,.86);border-radius:0 0 26px 26px;overflow:hidden}
.hero-panel .social-bar{position:absolute;left:0;bottom:0;width:100%;height:50px;background:var(--red-deep)}
.hero-title{position:absolute;left:390px;top:223px;color:var(--white);font-size:41px;line-height:48px;font-weight:400;width:460px}
.hero-title b{font-weight:700}
.hero-text{position:absolute;left:390px;top:374px;width:430px;color:var(--white);font-size:14.5px;line-height:17.5px}
.btn{position:absolute;display:flex;align-items:center;justify-content:center;text-decoration:none;color:var(--white);font-weight:700;border-radius:4px}
.btn-navy{left:521px;top:450px;width:166px;height:31px;background:var(--navy-btn);font-size:13px}
.btn-red{left:521px;top:491px;width:166px;height:41px;background:var(--red);font-size:16px;box-shadow:0 2px 4px rgba(0,0,0,.25)}
.social-link{position:absolute;top:587px;display:flex;align-items:center;gap:5px;color:var(--white);font-size:8px;line-height:9px;text-decoration:none}
.social-link .dot{width:18px;height:18px;border-radius:50%;background:#111}

/* partner strip */
.partners{position:absolute;left:0;top:589px;width:1200px;height:118px;background:var(--strip)}
.badge{position:absolute;background:#c9ccd6;border-radius:3px}

/* government section */
.gov{position:absolute;left:0;top:707px;width:1200px;height:438px;background:var(--navy);color:var(--white)}
.gov h2{position:absolute;left:159px;top:48px;font-size:26px;line-height:32px;font-weight:700}
.gov p{position:absolute;left:159px;top:129px;width:430px;font-size:12.5px;line-height:15px}
.gov-list{position:absolute;left:159px;top:225px;list-style:none}
.gov-list li{display:flex;align-items:center;gap:19px;height:35.7px;font-size:13px}
.gov-photo{position:absolute;left:635px;top:53px;width:499px;height:332px;background:linear-gradient(135deg,#3f4a46 0%,#9aa39e 40%,#d4d6d3 60%,#6e7670 100%)}

/* past contracts */
.contracts-title{position:absolute;left:0;width:1180px;top:1170px;text-align:center;font-size:26px;font-weight:700}
.contract{position:absolute;width:160px}
.contract h3{font-size:11px;line-height:15px;font-weight:700;margin-top:6px}
.contract small{display:block;font-size:8.5px;line-height:11px;color:var(--muted);margin-top:2px}
.view-all{position:absolute;left:833px;top:1372px;width:209px;height:117px;background:var(--red);border-radius:12px;color:var(--white);text-decoration:none;display:flex;align-items:center;gap:14px;padding-left:41px;font-size:16px;font-weight:700}

/* recruitment */
.recruit{position:absolute;left:0;top:1584px;width:1200px;height:865px;background:var(--grey)}
.recruit h2{position:absolute;left:0;width:1198px;top:22px;text-align:center;font-size:26px;font-weight:700}
.recruit .intro{position:absolute;left:390px;width:418px;top:68px;text-align:center;font-size:12.5px;line-height:15px;color:var(--muted)}
.card{position:absolute;width:284px;height:318px;background:var(--white);text-align:center}
.card svg.clock{position:absolute;left:111px;top:75px}
.card h3{position:absolute;left:0;width:100%;top:160px;font-size:20px;font-weight:700;color:var(--ink)}
.card p{position:absolute;left:0;width:100%;top:194px;font-size:15px;line-height:18px;color:var(--ink)}
.card .find{position:absolute;left:84px;top:260px;width:116px;height:19px;background:var(--red);border-radius:4px;color:var(--white);font-size:11px;line-height:19px;text-decoration:none;box-shadow:0 2px 3px rgba(0,0,0,.25)}
.card-brand{background:var(--navy)}
.card-brand span{position:absolute;left:0;width:100%;top:140px;color:var(--red);font-weight:900;font-size:22px}

/* footer */
.site-footer{position:absolute;left:0;top:2449px;width:1200px;height:382px;background:var(--footer);color:#cfcfcf;font-family:'Montserrat',sans-serif}
.footer-brand{position:absolute;left:174px;top:56px;color:var(--white);font-family:'Lato',sans-serif;font-weight:900;font-size:15px}
.footer-col{position:absolute;top:62px;list-style:none}
.footer-col h4{font-size:10.5px;font-weight:700;color:#e6e6e6;margin-bottom:20px}
.footer-col li{font-size:10px;line-height:25px;display:flex;align-items:center;gap:6px}
.footer-col .ring{width:9px;height:9px;border-radius:50%;border:2px solid #cfcfcf}
.footer-rule{position:absolute;left:176px;top:325px;width:848px;height:1px;background:#444}
.legal{position:absolute;right:176px;top:348px;display:flex;gap:16px;font-size:8.5px;color:#bdbdbd}
</style>
</head>
<body>

<header class="site-header">
  <div class="brand"><span class="mark"></span>Harbor Crest Solutions</div>
  <nav class="main-nav">
    <a style="left:533px;top:20px">Home</a>
    <a style="left:610px;top:20px">Recourses</a>
    <a style="left:715px;top:20px">Reviews</a>
    <a style="left:806px;top:20px">FAQ s</a>
    <a style="left:881px;top:20px">Contact</a>
  </nav>
  <svg class="menu-toggle" width="20" height="16" viewBox="0 0 20 16" aria-label="Menu">
    <g fill="var(--red)"><rect x="0" y="0" width="3" height="3"/><rect x="5" y="0" width="15" height="3"/><rect x="0" y="6" width="3" height="3"/><rect x="5" y="6" width="15" height="3"/><rect x="0" y="12" width="3" height="3"/><rect x="5" y="12" width="15" height="3"/></g>
  </svg>
</header>

<section class="hero">
  <div class="hero-photo" role="img" aria-label="Team collaborating in an office on the left and a confident professional woman with arms crossed on the right"></div>
</section>
<div class="hero-panel"><div class="social-bar"></div></div>
<h1 class="hero-title">Your trusted Partner in <b>Workforce, IT&nbsp; </b>&amp; <b>Logestic Solution</b></h1>
<p class="hero-text">We are an international staffing and professional services company dedicated to the belief that good people should be easy to find. Whether you need talent or transformation, let's grow together.</p>
<a class="btn btn-navy" href="#">Discover Our Services</a>
<a class="btn btn-red" href="#">Find a Job</a>
<a class="social-link" style="left:456px" href="#"><span class="dot"></span><span>www.work<br>vine.com</span></a>
<a class="social-link" style="left:531px" href="#"><span class="dot"></span><span>www.page<br>bloom.com</span></a>
<a class="social-link" style="left:607px" href="#"><span class="dot"></span><span>www.snap<br>nest.com</span></a>
<a class="social-link" style="left:681px" href="#"><span class="dot"></span><span>www.quil<br>lo.com</span></a>

<section class="partners" aria-label="Accreditations and memberships">
  <div class="badge" style="left:159px;top:57px;width:61px;height:23px"></div>
  <div class="badge" style="left:297px;top:55px;width:92px;height:24px"></div>
  <div class="badge" style="left:467px;top:58px;width:90px;height:20px"></div>
  <div class="badge" style="left:634px;top:50px;width:58px;height:36px;background:#b39a4a"></div>
  <div class="badge" style="left:769px;top:54px;width:92px;height:28px"></div>
  <div class="badge" style="left:937px;top:50px;width:46px;height:36px;border-radius:50% 50% 4px 4px"></div>
</section>

<section class="gov">
  <h2>Empowering Government Contracts<br>with Precision &amp; Performance</h2>
  <p>Unlock smarter, faster, and fully compliant contracting solutions tailored for federal, state, and local agencies.<br>&nbsp;Whether you're sourcing critical services, streamlining procurement, or navigating compliance, we're your trusted partner in driving government success.</p>
  <ul class="gov-list">
    <li><svg width="18" height="18" viewBox="0 0 18 18"><circle cx="9" cy="9" r="9" fill="var(--check)"/><path d="M5 9.2l2.7 2.6L13 6.5" stroke="#fff" stroke-width="1.8" fill="none"/></svg>Fast, Compliant Procurement Support</li>
    <li><svg width="18" height="18" viewBox="0 0 18 18"><circle cx="9" cy="9" r="9" fill="var(--check)"/><path d="M5 9.2l2.7 2.6L13 6.5" stroke="#fff" stroke-width="1.8" fill="none"/></svg>&nbsp;Registered &amp; Certified Vendor</li>
    <li><svg width="18" height="18" viewBox="0 0 18 18"><circle cx="9" cy="9" r="9" fill="var(--check)"/><path d="M5 9.2l2.7 2.6L13 6.5" stroke="#fff" stroke-width="1.8" fill="none"/></svg>&nbsp;Tailored Solutions for Federal, State &amp; Local Agencies</li>
    <li><svg width="18" height="18" viewBox="0 0 18 18"><circle cx="9" cy="9" r="9" fill="var(--check)"/><path d="M5 9.2l2.7 2.6L13 6.5" stroke="#fff" stroke-width="1.8" fill="none"/></svg>Deep Regulatory Knowledge</li>
    <li><svg width="18" height="18" viewBox="0 0 18 18"><circle cx="9" cy="9" r="9" fill="var(--check)"/><path d="M5 9.2l2.7 2.6L13 6.5" stroke="#fff" stroke-width="1.8" fill="none"/></svg>Streamlined Contract Management</li>
  </ul>
  <div class="gov-photo" role="img" aria-label="Smiling professional working on a laptop in a bright modern office"></div>
</section>

<h2 class="contracts-title">Past Contracts</h2>
<div class="contract" style="left:167px;top:1248px"><svg width="28" height="22" viewBox="0 0 28 22"><path d="M1 3h9l2 3h14v15H1z" fill="#111"/><path d="M4 9h23l-3 12H1z" fill="#111" stroke="#fff" stroke-width="1.2"/></svg><h3>Streamlined Contract<br>Management</h3><small>Streamlined Contract Management<br>Streamlined Contract Management</small></div>
<div class="contract" style="left:383px;top:1248px"><svg width="28" height="22" viewBox="0 0 28 22"><path d="M1 3h9l2 3h14v15H1z" fill="#111"/><path d="M4 9h23l-3 12H1z" fill="#111" stroke="#fff" stroke-width="1.2"/></svg><h3>Streamlined Contract<br>Management</h3><small>Streamlined Contract Management<br>Streamlined Contract Management</small></div>
<div class="contract" style="left:608px;top:1248px"><svg width="28" height="22" viewBox="0 0 28 22"><path d="M1 3h9l2 3h14v15H1z" fill="#111"/><path d="M4 9h23l-3 12H1z" fill="#111" stroke="#fff" stroke-width="1.2"/></svg><h3>Streamlined Contract<br>Management</h3><small>Streamlined Contract Management<br>Streamlined Contract Management</small></div>
<div class="contract" style="left:833px;top:1248px"><svg width="28" height="22" viewBox="0 0 28 22"><path d="M1 3h9l2 3h14v15H1z" fill="#111"/><path d="M4 9h23l-3 12H1z" fill="#111" stroke="#fff" stroke-width="1.2"/></svg><h3>Streamlined Contract<br>Management</h3><small>Streamlined Contract Management<br>Streamlined Contract Management</small></div>
<div class="contract" style="left:167px;top:1389px"><svg width="28" height="22" viewBox="0 0 28 22"><path d="M1 3h9l2 3h14v15H1z" fill="#111"/><path d="M4 9h23l-3 12H1z" fill="#111" stroke="#fff" stroke-width="1.2"/></svg><h3>Streamlined Contract<br>Management</h3><small>Streamlined Contract Management<br>Streamlined Contract Management</small></div>
<div class="contract" style="left:383px;top:1389px"><svg width="28" height="22" viewBox="0 0 28 22"><path d="M1 3h9l2 3h14v15H1z" fill="#111"/><path d="M4 9h23l-3 12H1z" fill="#111" stroke="#fff" stroke-width="1.2"/></svg><h3>Streamlined Contract<br>Management</h3><small>Streamlined Contract Management<br>Streamlined Contract Management</small></div>
<div class="contract" style="left:608px;top:1389px"><svg width="28" height="22" viewBox="0 0 28 22"><path d="M1 3h9l2 3h14v15H1z" fill="#111"/><path d="M4 9h23l-3 12H1z" fill="#111" stroke="#fff" stroke-width="1.2"/></svg><h3>Streamlined Contract<br>Management</h3><small>Streamlined Contract Management<br>Streamlined Contract Management</small></div>
<a class="view-all" href="#">View All <svg width="56" height="6" viewBox="0 0 56 6"><path d="M0 3h52" stroke="#fff" stroke-width="1"/><path d="M51 1l4 2-4 2z" fill="#fff"/></svg></a>

<section class="recruit">
  <h2>Recruitment Solutions</h2>
  <p class="intro">Unlock your business potential with our dedicated recruitment solutions. Learn more about our full catalog of offerings for organizations of any size across any industry.</p>
</section>

<div class="card" style="left:158px;top:1718px">
  <svg class="clock" width="62" height="62" viewBox="0 0 62 62"><circle cx="31" cy="33" r="27" fill="none" stroke="#111" stroke-width="3"/><circle cx="31" cy="33" r="19" fill="none" stroke="#111" stroke-width="2"/><path d="M31 22v11l7-5" stroke="#111" stroke-width="2" fill="none"/><rect x="27" y="2" width="8" height="4" fill="#111"/></svg>
  <h3>Flexible Placement</h3><p>Streamlined Contract Management<br>Streamlined Contract Management</p><a class="find" href="#">Find a Job</a>
</div>
<div class="card card-brand" style="left:458px;top:1718px"><span>HARBOR CREST SOLUTIONS</span></div>
<div class="card" style="left:758px;top:1718px">
  <svg class="clock" width="62" height="62" viewBox="0 0 62 62"><circle cx="31" cy="33" r="27" fill="none" stroke="#111" stroke-width="3"/><circle cx="31" cy="33" r="19" fill="none" stroke="#111" stroke-width="2"/><path d="M31 22v11l7-5" stroke="#111" stroke-width="2" fill="none"/><rect x="27" y="2" width="8" height="4" fill="#111"/></svg>
  <h3>Permanent Recruitment</h3><p>Streamlined Contract Management<br>Streamlined Contract Management</p><a class="find" href="#">Find a Job</a>
</div>
<div class="card" style="left:158px;top:2050px">
  <svg class="clock" width="62" height="62" viewBox="0 0 62 62"><circle cx="31" cy="33" r="27" fill="none" stroke="#111" stroke-width="3"/><circle cx="31" cy="33" r="19" fill="none" stroke="#111" stroke-width="2"/><path d="M31 22v11l7-5" stroke="#111" stroke-width="2" fill="none"/><rect x="27" y="2" width="8" height="4" fill="#111"/></svg>
  <h3>Diversity &amp; Inclusion</h3><p>Streamlined Contract Management<br>Streamlined Contract Management</p><a class="find" href="#">Find a Job</a>
</div>
<div class="card" style="left:458px;top:2050px">
  <svg class="clock" width="62" height="62" viewBox="0 0 62 62"><circle cx="31" cy="33" r="27" fill="none" stroke="#111" stroke-width="3"/><circle cx="31" cy="33" r="19" fill="none" stroke="#111" stroke-width="2"/><path d="M31 22v11l7-5" stroke="#111" stroke-width="2" fill="none"/><rect x="27" y="2" width="8" height="4" fill="#111"/></svg>
  <h3>Training</h3><p>Streamlined Contract Management<br>Streamlined Contract Management</p><a class="find" href="#">Find a Job</a>
</div>
<div class="card" style="left:758px;top:2050px">
  <svg class="clock" width="62" height="62" viewBox="0 0 62 62"><circle cx="31" cy="33" r="27" fill="none" stroke="#111" stroke-width="3"/><circle cx="31" cy="33" r="19" fill="none" stroke="#111" stroke-width="2"/><path d="M31 22v11l7-5" stroke="#111" stroke-width="2" fill="none"/><rect x="27" y="2" width="8" height="4" fill="#111"/></svg>
  <h3>Outsourcing</h3><p>Streamlined Contract Management<br>Streamlined Contract Management</p><a class="find" href="#">Find a Job</a>
</div>

<footer class="site-footer">
  <div class="footer-brand">HARBOR CREST SOLUTIONS</div>
  <ul class="footer-col" style="left:423px"><h4>Built For Creatives</h4><li>Try Stackfold Pro</li><li>Find Inspiration</li><li>Get Hired</li><li>Sell Creative Assets</li><li>Sell Freelance Services</li></ul>
  <ul class="footer-col" style="left:581px"><h4>Find Talent</h4><li>Post a Job</li><li>Graphic Designers</li><li>Photographers</li><li>Video Editors</li><li>Web Designers</li><li>Illustrators</li></ul>
  <ul class="footer-col" style="left:740px"><h4>Stackfold</h4><li>About Stackfold</li><li>Corvell Portfolio</li><li>Download the App</li><li>Blog</li><li>Careers</li><li>Help Center</li><li>Contact Us</li></ul>
  <ul class="footer-col" style="left:898px"><h4>Social</h4><li><span class="ring"></span>Snapnest</li><li><span class="ring"></span>Quillo</li><li><span class="ring"></span>Pinwell</li><li><span class="ring"></span>Pagebloom</li><li><span class="ring"></span>Workvine</li></ul>
  <div class="footer-rule"></div>
  <div class="legal"><span>English ▾</span><span>TOU</span><span>Privacy</span><span>Community</span><span>Cookie preferences</span><span>Do not sell or share my personal information</span></div>
</footer>

</body>
</html>
```